RTW Business Card Design

We are an independent auto dealer who specializes in commercial & fleet vehicles, we are family owned and operated and have been in business since 2001. We stock late model, low mileage, white trucks & vans. We mostly deal with companies in the construction and service industries. We are just looking to try to freshen up our old business card, we do not want to change the logo at this point, because it is well know within the southwest region & construction community. I have attached our logo and a PDF of our current business card for reference.
Updates
If the address is stacked there is no comma (,) after NE. Everyone keeps putting it in with this format and it is not correct.
842 Ventana Blvd NE
Albuquerque, NM 87120
If the address is all on one line, then there will be a comma (,) after NE
842 Ventana Blvd NE, Albuquerque, NM 87120
Please make changes accordingly, thank you for your attention in this matter.
Industry/Entity Type
Construction
Contact Information for Business Card
842 Ventana Blvd NE, Albuquerque, NM 87120, Marcus Delaney, Vice President, marcus@rtwvehicledepot.com, www.RTWvehicledepot.com, ph 505-610-2247, fax 505-472-8156, cell 505-238-6094
Look and feel
Each slider illustrates characteristics of the customer's brand and the style your logo design should communicate.

```html
<!DOCTYPE html>
<html lang="en">
<head>
<meta charset="utf-8">
<title>RTW – Business Card</title>
<link rel="stylesheet" href="https://fonts.googleapis.com/css2?family=Cinzel:wght@500&family=Questrial&display=swap">
<style>
  :root {
    --backdrop: #d9d9d9;
    --card: #f3f3f3;
    --ink: #2a2a2a;
    --ink-soft: #4a4a4a;
    --brand-red: #d9242b;
    --on-red: #ffffff;
  }
  * { margin: 0; padding: 0; box-sizing: border-box; }
  html, body {
    width: 1200px; height: 900px; overflow: hidden;
    background: var(--backdrop);
  }
  .business-card {
    position: absolute; left: 75px; top: 150px;
    width: 1050px; height: 600px;
    background: var(--card);
    overflow: hidden;
    box-shadow: 0 6px 18px rgba(0,0,0,0.18);
  }
  .red-sweep { position: absolute; left: 0; top: 0; width: 1050px; height: 600px; }

  .brand-name {
    position: absolute; left: 110px; top: 165px;
    font-family: "Cinzel", serif; font-weight: 500;
    font-size: 84px; letter-spacing: 2px; line-height: 1;
    color: var(--ink);
  }

  .contact-block {
    position: absolute; left: 470px; top: 195px;
    font-family: "Questrial", sans-serif; color: var(--ink-soft);
  }
  .person-name {
    font-family: "Cinzel", serif; font-weight: 500;
    font-size: 30px; letter-spacing: 3px; color: var(--ink);
  }
  .person-title { font-size: 21px; color: var(--brand-red); margin-top: 2px; }
  .address { font-size: 18px; margin-top: 26px; letter-spacing: 0.5px; }
  .contact-list { list-style: none; margin-top: 10px; }
  .contact-list li {
    display: flex; align-items: center; gap: 14px;
    font-size: 18px; height: 32px; letter-spacing: 0.5px;
  }
  .contact-list svg { width: 20px; height: 20px; flex: none; }

  .website {
    position: absolute; left: 440px; right: 0; bottom: 22px;
    text-align: center;
    font-family: "Questrial", sans-serif; font-size: 26px;
    color: var(--on-red); letter-spacing: 1px;
  }
</style>
</head>
<body>
  <div class="business-card">
    <svg class="red-sweep" viewBox="0 0 1050 600" aria-hidden="true">
      <path d="M300 600 C340 540 370 512 440 512 L1050 512 L1050 600 Z" fill="var(--brand-red)"/>
    </svg>

    <p class="brand-name">RTW</p>

    <div class="contact-block">
      <p class="person-name">Marcus Delaney</p>
      <p class="person-title">Vice President</p>
      <p class="address">842 Ventana Blvd NE, Albuquerque, NM 87120</p>
      <ul class="contact-list">
        <li>
          <svg viewBox="0 0 20 20" aria-label="phone"><path d="M5 2 L8 2 L9 6 L7 8 C8 11 9 12 12 13 L14 11 L18 12 L18 15 C18 17 16 18 14 18 C8 17 3 12 2 6 C2 4 3 2 5 2 Z" fill="none" stroke="var(--brand-red)" stroke-width="1.6"/></svg>
          505-610-2247
        </li>
        <li>
          <svg viewBox="0 0 20 20" aria-label="fax"><rect x="3" y="8" width="14" height="9" fill="none" stroke="var(--brand-red)" stroke-width="1.6"/><rect x="6" y="3" width="8" height="5" fill="none" stroke="var(--brand-red)" stroke-width="1.6"/><line x1="6" y1="13" x2="14" y2="13" stroke="var(--brand-red)" stroke-width="1.6"/></svg>
          505-472-8156
        </li>
        <li>
          <svg viewBox="0 0 20 20" aria-label="cell"><rect x="6" y="2" width="8" height="16" rx="1.5" fill="none" stroke="var(--brand-red)" stroke-width="1.6"/><line x1="9" y1="15" x2="11" y2="15" stroke="var(--brand-red)" stroke-width="1.6"/></svg>
          505-238-6094
        </li>
        <li>
          <svg viewBox="0 0 20 20" aria-label="email"><rect x="2" y="5" width="16" height="11" fill="none" stroke="var(--brand-red)" stroke-width="1.6"/><path d="M2 5 L10 11 L18 5" fill="none" stroke="var(--brand-red)" stroke-width="1.6"/></svg>
          marcus@rtwvehicledepot.com
        </li>
      </ul>
    </div>

    <p class="website">www.RTWvehicledepot.com</p>
  </div>
</body>
</html>
```